Copper Fern Photography

Internet sales of landscape photography
Some background on the name.... I'm originally from Kentucky hence the "Copper" and I now live in California wine country, hence the "Fern." The blue coloring in the name is from the Halverton Otters and the name "photography" is done in a bourbon lettering font. Hope this helps.
Updates
Please include email as dennis@copperfernstudio.test
Please make website www.copperfernstudio.test and ad QR code if possible.
Industry/Entity Type
Landscape
Contact Information for Business Card
Dennis Marlow
www.copperfernpix.test
555-014-2297
Requirements
Must have
- My design logo, all contact info :)
I like the thought of a QR Code along with the written link also.

```html
<!DOCTYPE html>
<html lang="en">
<head>
<meta charset="utf-8">
<title>Copper Fern Photography – Business Card</title>
<link rel="stylesheet" href="https://fonts.googleapis.com/css2?family=Exo:wght@500;600&family=Quicksand:wght@500&display=swap">
<style>
  :root {
    --backdrop: #5a5a5a;
    --card-white: #ffffff;
    --brand-blue: #125eab;
    --divider: #111111;
    --on-blue: #ffffff;
  }
  * { box-sizing: border-box; margin: 0; padding: 0; }
  html, body {
    width: 1200px;
    height: 1000px;
    overflow: hidden;
    background: var(--backdrop);
  }
  .canvas {
    position: relative;
    width: 1200px;
    height: 1000px;
  }
  .business-card {
    position: absolute;
    left: 150px;
    top: 236px;
    width: 900px;
    height: 528px;
    background: var(--card-white);
    display: flex;
    flex-direction: column;
  }
  .card-brand {
    height: 332px;
    display: flex;
    align-items: center;
    justify-content: center;
    gap: 22px;
  }
  .brand-mark {
    width: 46px;
    height: 46px;
    border-radius: 50%;
    background: var(--brand-blue);
    flex: none;
  }
  .brand-name {
    font-family: "Exo", sans-serif;
    font-weight: 600;
    font-size: 54px;
    color: var(--brand-blue);
    letter-spacing: 1px;
  }
  .card-divider {
    height: 8px;
    background: var(--divider);
  }
  .card-contact {
    flex: 1;
    background: var(--brand-blue);
    display: flex;
    align-items: center;
    padding: 0 40px 0 68px;
    color: var(--on-blue);
  }
  .holder-name {
    font-family: "Exo", sans-serif;
    font-weight: 500;
    font-size: 40px;
    letter-spacing: 1.5px;
    width: 320px;
    flex: none;
    white-space: nowrap;
  }
  .contact-list {
    list-style: none;
    font-family: "Quicksand", sans-serif;
    font-weight: 500;
    font-size: 22px;
    display: flex;
    flex-direction: column;
    gap: 8px;
    flex: 1;
    white-space: nowrap;
  }
  .contact-item {
    display: flex;
    align-items: center;
    gap: 10px;
  }
  .contact-icon {
    width: 20px;
    height: 20px;
    flex: none;
  }
  .qr-code {
    width: 128px;
    height: 128px;
    background: var(--card-white);
    border-radius: 4px;
    flex: none;
  }
</style>
</head>
<body>
<div class="canvas">
  <div class="business-card">
    <div class="card-brand">
      <span class="brand-mark"></span>
      <span class="brand-name">Copper Fern Photography</span>
    </div>
    <div class="card-divider"></div>
    <div class="card-contact">
      <div class="holder-name">Dennis Marlow</div>
      <ul class="contact-list">
        <li class="contact-item">
          <svg class="contact-icon" viewBox="0 0 22 22" aria-hidden="true">
            <rect x="0" y="0" width="22" height="22" rx="4" fill="#fff"/>
            <path d="M7 4.5c1 0 1.6 2.6 1.6 3.2 0 .8-1.3 1-1.1 1.9.5 1.8 1.9 3.4 3.5 4.2.8.3 1.1-1 1.9-1 .6 0 3 .9 2.9 1.9-.1 1.3-1.5 2.5-2.9 2.3C8.6 18.4 4.9 13.6 4.6 8.4 4.5 6.6 5.7 4.5 7 4.5z" fill="#125eab"/>
          </svg>
          <span>555-014-2297</span>
        </li>
        <li class="contact-item">
          <svg class="contact-icon" viewBox="0 0 22 22" aria-hidden="true">
            <rect x="0" y="0" width="22" height="22" rx="4" fill="#fff"/>
            <rect x="4" y="6" width="14" height="10" rx="1" fill="none" stroke="#125eab" stroke-width="1.4"/>
            <path d="M4.5 6.8 11 12l6.5-5.2" fill="none" stroke="#125eab" stroke-width="1.4"/>
          </svg>
          <span>dennis@copperfernstudio.test</span>
        </li>
        <li class="contact-item">
          <svg class="contact-icon" viewBox="0 0 22 22" aria-hidden="true">
            <rect x="0" y="0" width="22" height="22" rx="4" fill="#fff"/>
            <g fill="none" stroke="#125eab" stroke-width="1.4">
              <circle cx="11" cy="11" r="6.5"/>
              <ellipse cx="11" cy="11" rx="2.8" ry="6.5"/>
              <line x1="4.5" y1="11" x2="17.5" y2="11"/>
            </g>
          </svg>
          <span>www.copperfernstudio.test</span>
        </li>
      </ul>
      <div class="qr-code" role="img" aria-label="QR code linking to www.copperfernstudio.test"></div>
    </div>
  </div>
</div>
</body>
</html>
```